bail bonds business

Need a web design for a Bail Bond company. At Larkmoor Bails, we specialize in getting arrested defendants out of jail. Also, I have all the necessary information already uploaded in the files.

Target Market(s)

Arrested defendants and their families who will post bails on their behalf.

Industry/Entity Type

Business

Coding

Coded - Design and coding required

Number of Pages Required

1 page

```html
<!DOCTYPE html>
<html lang="en">
<head>
<meta charset="utf-8">
<title>Larkmoor Bails</title>
<link rel="stylesheet" href="https://fonts.googleapis.com/css2?family=Oswald:wght@400;500;700&family=Roboto:wght@300;400;500;700&display=swap">
<style>
:root{
  --red:#c4161c;
  --red-dark:#9e1015;
  --ink:#333;
  --muted:#8a8a8a;
  --light:#ececec;
  --card:#f7f7f7;
  --footer:#2a2a2a;
  --footer-deep:#1f1f1f;
  --white:#fff;
}
*{box-sizing:border-box;margin:0;padding:0}
html,body{width:784px;height:1200px;overflow:hidden}
body{font-family:"Roboto",sans-serif;color:var(--ink);background:var(--white);position:relative}

/* header */
.site-header{height:90px;display:flex;align-items:center;justify-content:space-between;padding:0 50px 0 40px;background:var(--white)}
.brand{display:flex;align-items:center;gap:8px;font-family:"Oswald",sans-serif;font-weight:700;font-size:19px;color:var(--red);letter-spacing:.5px;text-transform:uppercase}
.brand-dot{width:14px;height:14px;border-radius:50%;background:var(--red)}
.main-nav{display:flex;align-items:center;gap:8px}
.main-nav a{font-size:11px;font-weight:500;color:var(--ink);text-decoration:none;padding:9px 17px;border:1px solid transparent;text-transform:uppercase}
.main-nav a.active{border-color:var(--red);color:var(--red);border-radius:2px}
.search-btn{width:30px;height:30px;border-radius:50%;background:#9a9a9a;display:flex;align-items:center;justify-content:center;margin-left:10px}

/* hero */
.hero{position:relative;height:380px;overflow:hidden}
.hero-photo{position:absolute;inset:0;background:linear-gradient(110deg,#6f7780 0%,#a9b0b8 35%,#d9dde2 55%,#7f8fa6 75%,#3a4a6b 100%)}
.hero-copy{position:absolute;left:44px;top:70px;color:var(--white)}
.hero-title{font-family:"Oswald",sans-serif;font-weight:700;font-size:112px;line-height:1;letter-spacing:1px}
.hero-sub{font-family:"Oswald",sans-serif;font-weight:500;font-size:30px;letter-spacing:1px;margin-top:4px}
.hero-tag{font-family:"Roboto",sans-serif;font-weight:300;font-size:15px;letter-spacing:9px;margin-top:18px}
.hero-arrows{position:absolute;left:66px;bottom:20px;display:flex;gap:8px}
.hero-arrows span{width:26px;height:26px;border-radius:50%;border:2px solid var(--red);display:flex;align-items:center;justify-content:center;background:rgba(255,255,255,.2)}

/* welcome band */
.welcome{height:130px;background:var(--red);display:flex;color:var(--white)}
.welcome-title{width:215px;background:var(--red-dark);font-family:"Oswald",sans-serif;font-weight:500;font-size:22px;line-height:1.25;padding:38px 0 0 40px;position:relative}
.welcome-title::after{content:"";position:absolute;right:-22px;top:0;border-top:65px solid transparent;border-bottom:65px solid transparent;border-left:22px solid var(--red-dark)}
.welcome-points{list-style:none;padding:12px 40px 0 52px;flex:1}
.welcome-points li{display:flex;gap:10px;margin-bottom:6px}
.welcome-points svg{flex:none;margin-top:2px}
.welcome-points h3{font-size:10.5px;font-weight:700}
.welcome-points p{font-size:7.5px;line-height:1.3;opacity:.9}

/* services */
.services{height:210px;background:var(--light);display:flex;gap:8px;padding:22px 36px 0 36px}
.service-card{flex:1;height:158px;background:var(--card);border-bottom:3px solid var(--red);text-align:center;padding-top:16px}
.service-icon{width:54px;height:54px;border-radius:50%;border:2px solid var(--red);margin:0 auto 12px;display:flex;align-items:center;justify-content:center;background:var(--white)}
.service-card h4{font-size:11px;font-weight:700;text-transform:uppercase;color:var(--ink)}
.service-card p{font-size:7.5px;color:var(--muted);line-height:1.35;margin:8px auto 0;width:120px}

/* offer */
.offer{height:270px;display:flex;padding:22px 36px 0 50px;gap:34px}
.offer-photo{width:340px;height:220px;background:linear-gradient(120deg,#5a6a80 0%,#aab6c3 45%,#e4e6e9 70%,#6d7480 100%)}
.offer-body{flex:1}
.offer-title{font-family:"Oswald",sans-serif;font-weight:500;font-size:24px;line-height:1.2;color:var(--ink)}
.offer-lead{font-family:"Oswald",sans-serif;font-size:13px;color:var(--red);margin-top:2px}
.offer-list{list-style:none;margin-top:12px}
.offer-list li{font-size:8.5px;color:var(--ink);display:flex;align-items:center;gap:7px;margin-bottom:5px}
.offer-list li::before{content:"";width:5px;height:5px;border-radius:50%;background:var(--red)}
.notary{margin-top:10px;border:1px solid var(--red);display:flex;align-items:center;gap:10px;padding:7px 10px;width:250px}
.notary-badge{flex:none;width:30px;height:30px;border-radius:50%;border:2px solid var(--ink);font-family:"Oswald",sans-serif;font-weight:700;font-size:12px;display:flex;align-items:center;justify-content:center}
.notary strong{display:block;font-family:"Oswald",sans-serif;font-size:11px;color:var(--red);font-weight:500}
.notary span{display:block;font-family:"Oswald",sans-serif;font-size:12px;color:var(--ink)}
.notary small{display:block;font-size:7px;color:var(--muted);margin-top:2px}

/* footer */
.site-footer{height:120px;background:var(--footer);color:#cfcfcf;position:relative;padding:18px 36px 0 36px}
.footer-title{font-size:12px;font-weight:700;color:var(--white)}
.footer-contact{font-size:8px;margin-top:8px;line-height:1.9}
.footer-contact .row{display:flex;gap:26px}
.social{position:absolute;right:56px;top:34px;display:flex;gap:8px}
.social span{width:26px;height:26px;border-radius:50%;border:1.5px solid #d0d0d0;display:flex;align-items:center;justify-content:center}
.footer-bottom{position:absolute;left:0;right:0;bottom:0;height:30px;background:var(--footer-deep);font-size:7.5px;color:#9a9a9a;display:flex;align-items:center;padding:0 36px}
</style>
</head>
<body>

<header class="site-header">
  <div class="brand"><span class="brand-dot"></span>Larkmoor Bails</div>
  <nav class="main-nav">
    <a href="#" class="active">Home</a>
    <a href="#">About</a>
    <a href="#">Services</a>
    <a href="#">Contact</a>
    <span class="search-btn">
      <svg width="12" height="12" viewBox="0 0 12 12"><circle cx="5" cy="5" r="3.6" fill="none" stroke="#fff" stroke-width="1.6"/><line x1="7.7" y1="7.7" x2="11" y2="11" stroke="#fff" stroke-width="1.8"/></svg>
    </span>
  </nav>
</header>

<section class="hero">
  <div class="hero-photo" role="img" aria-label="Close-up of a police car with its blue roof lights flashing"></div>
  <div class="hero-copy">
    <h1 class="hero-title">BAILS</h1>
    <p class="hero-sub">WE BRING FAMILIES TOGETHER</p>
    <p class="hero-tag">PROFESSIONAL &nbsp; AND &nbsp; EFFECTIVE</p>
  </div>
  <div class="hero-arrows">
    <span><svg width="8" height="8" viewBox="0 0 8 8"><path d="M5.5 1 2.5 4l3 3" fill="none" stroke="#c4161c" stroke-width="1.6"/></svg></span>
    <span><svg width="8" height="8" viewBox="0 0 8 8"><path d="M2.5 1l3 3-3 3" fill="none" stroke="#c4161c" stroke-width="1.6"/></svg></span>
  </div>
</section>

<section class="welcome">
  <h2 class="welcome-title">WELCOME TO<br>LARKMOOR BAILS</h2>
  <ul class="welcome-points">
    <li>
      <svg width="9" height="9" viewBox="0 0 8 8"><path d="M2 1l3 3-3 3" fill="none" stroke="#fff" stroke-width="1.6"/></svg>
      <div><h3>Your freedom starts with Larkmoor!</h3><p>Many defendants wait days in jail simply because no one knows the process. We explain every step and start right away.</p></div>
    </li>
    <li>
      <svg width="9" height="9" viewBox="0 0 8 8"><path d="M2 1l3 3-3 3" fill="none" stroke="#fff" stroke-width="1.6"/></svg>
      <div><h3>Larkmoor gets you out. Larkmoor gets you home</h3><p>Call us day or night and an agent will meet you, review the charges and post the bond quickly.</p></div>
    </li>
    <li>
      <svg width="9" height="9" viewBox="0 0 8 8"><path d="M2 1l3 3-3 3" fill="none" stroke="#fff" stroke-width="1.6"/></svg>
      <div><h3>We guarantee your bail</h3><p>Our fees are set by state law and we never add hidden costs to your family's bill.</p></div>
    </li>
  </ul>
</section>

<section class="services">
  <article class="service-card">
    <div class="service-icon"><svg width="26" height="16" viewBox="0 0 26 16"><circle cx="7" cy="8" r="5" fill="none" stroke="#c4161c" stroke-width="2"/><circle cx="19" cy="8" r="5" fill="none" stroke="#c4161c" stroke-width="2"/><line x1="12" y1="8" x2="14" y2="8" stroke="#c4161c" stroke-width="2"/></svg></div>
    <h4>Felony Bails</h4>
    <p>Effective counsel and fast release for felony cases</p>
  </article>
  <article class="service-card">
    <div class="service-icon"><svg width="22" height="22" viewBox="0 0 22 22"><rect x="5" y="8" width="12" height="6" rx="3" fill="none" stroke="#c4161c" stroke-width="2" transform="rotate(-40 11 11)"/></svg></div>
    <h4>Drug Charges Bails</h4>
    <p>Discreet help and quick bonds for drug charges</p>
  </article>
  <article class="service-card">
    <div class="service-icon"><svg width="22" height="22" viewBox="0 0 22 22"><circle cx="11" cy="11" r="8" fill="none" stroke="#c4161c" stroke-width="2"/><line x1="11" y1="6" x2="11" y2="12" stroke="#c4161c" stroke-width="2"/><circle cx="11" cy="15.5" r="1.3" fill="#c4161c"/></svg></div>
    <h4>Sex Crime Bails</h4>
    <p>Private, respectful service for sensitive criminal charges</p>
  </article>
  <article class="service-card">
    <div class="service-icon"><svg width="22" height="22" viewBox="0 0 22 22"><path d="M4 14l2-6h10l2 6z" fill="none" stroke="#c4161c" stroke-width="2"/><circle cx="7" cy="16" r="1.6" fill="#c4161c"/><circle cx="15" cy="16" r="1.6" fill="#c4161c"/></svg></div>
    <h4>DUI Bails</h4>
    <p>Fast release after driving under the influence arrests</p>
  </article>
</section>

<section class="offer">
  <div class="offer-photo" role="img" aria-label="Police officer placing a handcuffed man against a patrol car"></div>
  <div class="offer-body">
    <h2 class="offer-title">WHAT WE OFFER</h2>
    <p class="offer-lead">AT LARKMOOR BAILS, WE DEAL WITH</p>
    <ul class="offer-list">
      <li>Felony bails</li>
      <li>Drug Charges bails</li>
      <li>Sex Crime bails</li>
      <li>DUI bails</li>
      <li>Theft bails</li>
    </ul>
    <div class="notary">
      <div class="notary-badge">24</div>
      <div><strong>24/7 · NOTARY PUBLIC SERVICE</strong><span>SERVING ALL OF WESTERN NEW YORK</span><small>All our agents are licensed, bonded and ready to help.</small></div>
    </div>
  </div>
</section>

<footer class="site-footer">
  <h3 class="footer-title">CONTACT</h3>
  <div class="footer-contact">
    <div>148 Harrow Street, Suite 40, Larkmoor, NY 14201</div>
    <div class="row"><span>716-555-0148</span><span>716-555-0192</span><span>info@larkmoorbails.com</span></div>
  </div>
  <div class="social" aria-label="Contact links">
    <span><svg width="12" height="12" viewBox="0 0 12 12"><path d="M3 1.5h2l1 2.5-1.3.9a6 6 0 0 0 2.4 2.4L8 6l2.5 1v2c0 .8-.7 1.5-1.5 1.5A8 8 0 0 1 1.5 3c0-.8.7-1.5 1.5-1.5z" fill="#d0d0d0"/></svg></span>
    <span><svg width="12" height="12" viewBox="0 0 12 12"><rect x="1" y="2.5" width="10" height="7" fill="none" stroke="#d0d0d0" stroke-width="1.2"/><path d="M1 3l5 3.5L11 3" fill="none" stroke="#d0d0d0" stroke-width="1.2"/></svg></span>
    <span><svg width="12" height="12" viewBox="0 0 12 12"><path d="M6 11S2.5 7 2.5 4.5a3.5 3.5 0 0 1 7 0C9.5 7 6 11 6 11z" fill="#d0d0d0"/><circle cx="6" cy="4.5" r="1.2" fill="#2a2a2a"/></svg></span>
    <span><svg width="12" height="12" viewBox="0 0 12 12"><path d="M1.5 2h9v6h-5l-2.5 2V8h-1.5z" fill="none" stroke="#d0d0d0" stroke-width="1.2"/></svg></span>
    <span><svg width="12" height="12" viewBox="0 0 12 12"><circle cx="6" cy="6" r="4.5" fill="none" stroke="#d0d0d0" stroke-width="1.2"/><path d="M6 3.5V6l2 1.5" fill="none" stroke="#d0d0d0" stroke-width="1.2"/></svg></span>
  </div>
  <div class="footer-bottom">Copyright © 2024 · Larkmoor Bails · All Rights Reserved</div>
</footer>

</body>
</html>
```